Herbal tea packaging using a kraft stand up pouch

We would like a design for our tea bags. We want the consumer to understand that our products are natural just by looking at the bag. The bag will be a kraft stand up pouch, I thought this information might help with choosing the colors. The maximum number of colors we want is 3. Our logo is already 2 colors + 1 more for the design of the pouch. For your reference, we will add a sticker with the name of the tea on each pouch (like images no. 1(3) and 1(18)). We can't yet print in 4 colors and we would like the name of the tea to be in a different color, so, for now, the sticker will do.

I am attaching some ideas that we like. We would really like something in those lines. The stand-up pouch will have a customized window at the front (so that the tea leaves are visible). One idea that we had is that the window could be in the shape of a leaf (like image no. 1(11)) and be surrounded by other drawn tea leaves (like in the other images with the drawn people and plants). We are open to any suggestions and ideas about the window and the drawing.

We already have our logo so I am attaching that as well (image named vel sarna logo). That would go on the front of the pouch, on top of the window.

We like the idea of a drawing on the front of the pouch like in the images we have attached. On the back of the pouch, we want to have directions on how to make the tea like in image no. 1(16) . We would also have paragraphs with an empty square on the front for each of our teas (like image no. 1(6)) but the text would be added on to it later. For now just 3-4 lines of sample text is fine for 4 different teas. The pouch material is food grade approved and recyclable, but cannot biodegradable, and it has KWR and HPM certificates. We think that would be a nice addition to the back of the pouch to inform the consumer.

I am also attaching the empty template of the pouch sent to us by the factory (pdf file 1(17)). We are not sure exactly about the size of the pouch but that shouldn't be a problem as we can adjust the dimensions accordingly.

Thanks a lot. For any questions, please contact me.

Target Market(s)

Tea lovers

Industry/Entity Type

Consumer

Font styles to use
Other font styles liked:
• a font that would go well with the logo

Colors
acd036
33b8a4
000000
333333
474747

Requirements
Must have
• Natural colors, a window at the front of the bag as described above, a drawing at the front as described above
Nice to have
• we would like the consumer to get the idea that our products are natural just by looking at the package. We are open to any suggestions you may have

```html
<!DOCTYPE html>
<html lang="en">
<head>
<meta charset="utf-8">
<title>Vel Sarna – Herbal Tea Pouch, Front and Back</title>
<link rel="stylesheet" href="https://fonts.googleapis.com/css2?family=Crimson+Text:wght@400;600&family=Handlee&display=swap">
<style>
  :root {
    --backdrop: #c9cbc4;
    --kraft-light: #dcb57a;
    --kraft: #cfa364;
    --kraft-dark: #b98c4f;
    --leaf-green: #8cbf2f;
    --tea-teal: #2f9e88;
    --tea-teal-deep: #1f7f6c;
    --logo-ink: #5d7a70;
    --script-ink: #7f6f52;
    --leaf-dark: #2a2621;
    --cert-ink: #474747;
  }
  * { box-sizing: border-box; margin: 0; padding: 0; }
  html, body { width: 1200px; height: 1200px; overflow: hidden; }
  body {
    background: var(--backdrop);
    position: relative;
    font-family: "Crimson Text", Georgia, serif;
  }
  .pouch {
    position: absolute;
    top: 272px;
    width: 460px;
    height: 684px;
    border-radius: 3px 3px 18px 18px;
    background: linear-gradient(100deg, var(--kraft-dark) 0%, var(--kraft-light) 30%, var(--kraft) 60%, var(--kraft-dark) 100%);
    overflow: hidden;
  }
  .pouch--front { left: 112px; }
  .pouch--back { left: 650px; width: 462px; }

  .tea-label {
    position: absolute;
    left: 150px; top: 0;
    width: 160px; height: 50px;
    background: var(--leaf-green);
    color: #fff;
    font-size: 24px;
    line-height: 50px;
    text-align: center;
  }
  .zip-seal {
    position: absolute;
    left: 0; right: 0; top: 76px;
    height: 2px;
    background: rgba(120, 85, 40, 0.25);
  }
  .brand {
    position: absolute;
    left: 150px; top: 84px;
    width: 160px; height: 170px;
    display: flex; flex-direction: column; align-items: center; justify-content: center;
    gap: 14px;
  }
  .brand__square {
    width: 96px; height: 96px;
    border: 3px solid var(--logo-ink);
  }
  .brand__name {
    color: var(--logo-ink);
    font-size: 22px;
    letter-spacing: 1px;
    text-transform: uppercase;
  }
  .front-copy {
    position: absolute;
    left: 204px; top: 296px;
    width: 190px;
    font-family: "Handlee", cursive;
    font-size: 12px;
    line-height: 13.5px;
    color: var(--script-ink);
  }
  .front-art { position: absolute; left: 0; top: 0; }

  .back-copy {
    position: absolute;
    left: 0; right: 0; top: 300px;
    text-align: center;
    font-family: "Handlee", cursive;
    font-size: 18px;
    line-height: 24px;
    color: var(--script-ink);
  }
  .brew-steps {
    position: absolute;
    left: 157px; top: 450px;
    display: flex; gap: 5px;
  }
  .brew-step {
    width: 46px; height: 74px;
    border: 2px solid var(--logo-ink);
    border-radius: 4px;
    position: relative;
  }
  .brew-step svg { position: absolute; left: 5px; top: 8px; }
  .brew-step__label {
    position: absolute;
    left: 2px; right: 2px; bottom: 2px;
    background: var(--logo-ink);
    color: #fff;
    font-size: 8px;
    font-weight: 600;
    text-align: center;
    line-height: 13px;
  }
  .net-weight {
    position: absolute;
    left: 0; right: 0; top: 548px;
    text-align: center;
    font-family: "Handlee", cursive;
    font-size: 16px;
    color: var(--script-ink);
  }
  .back-art { position: absolute; left: 0; top: 0; }
  .certs {
    position: absolute;
    left: 186px; top: 626px;
    display: flex; gap: 44px;
  }
  .cert-badge {
    width: 22px; height: 22px;
    border-radius: 50%;
    background: var(--cert-ink);
  }
</style>
</head>
<body>

  <section class="pouch pouch--front">
    <svg class="front-art" width="460" height="684" viewBox="0 0 460 684">
      <defs>
        <linearGradient id="plantationTone" x1="0" y1="0" x2="0" y2="1">
          <stop offset="0" stop-color="#2f9e88" stop-opacity="0.35"/>
          <stop offset="0.45" stop-color="#2f9e88" stop-opacity="0.8"/>
          <stop offset="1" stop-color="#1f7f6c" stop-opacity="0.95"/>
        </linearGradient>
      </defs>
      <path role="img" aria-label="Engraved-style illustration of tea pickers working on a hillside plantation, surrounded by tea bushes"
            d="M0,300 C40,290 90,290 110,320 C150,380 220,410 300,390 C360,375 410,360 460,340 L460,684 L0,684 Z"
            fill="url(#plantationTone)"/>
      <g role="img" aria-label="Scalloped window showing the loose dark tea leaves inside the pouch">
        <circle cx="224" cy="496" r="60" fill="var(--tea-teal)"/>
        <circle cx="224" cy="448" r="22" fill="var(--tea-teal)"/>
        <circle cx="224" cy="544" r="22" fill="var(--tea-teal)"/>
        <circle cx="176" cy="496" r="22" fill="var(--tea-teal)"/>
        <circle cx="272" cy="496" r="22" fill="var(--tea-teal)"/>
        <circle cx="190" cy="462" r="22" fill="var(--tea-teal)"/>
        <circle cx="258" cy="462" r="22" fill="var(--tea-teal)"/>
        <circle cx="190" cy="530" r="22" fill="var(--tea-teal)"/>
        <circle cx="258" cy="530" r="22" fill="var(--tea-teal)"/>
        <circle cx="224" cy="496" r="54" fill="var(--leaf-dark)"/>
        <circle cx="224" cy="452" r="18" fill="var(--leaf-dark)"/>
        <circle cx="224" cy="540" r="18" fill="var(--leaf-dark)"/>
        <circle cx="180" cy="496" r="18" fill="var(--leaf-dark)"/>
        <circle cx="268" cy="496" r="18" fill="var(--leaf-dark)"/>
        <circle cx="193" cy="465" r="18" fill="var(--leaf-dark)"/>
        <circle cx="255" cy="465" r="18" fill="var(--leaf-dark)"/>
        <circle cx="193" cy="527" r="18" fill="var(--leaf-dark)"/>
        <circle cx="255" cy="527" r="18" fill="var(--leaf-dark)"/>
      </g>
    </svg>
    <div class="tea-label">Lorem ipsum</div>
    <div class="zip-seal"></div>
    <div class="brand">
      <div class="brand__square"></div>
      <div class="brand__name">Vel Sarna</div>
    </div>
    <p class="front-copy">Lorem ipsum dolor sit amet, an harum nominavi vulputate duo, qui ne legere tempor ocurreret, at rebum feugait percipitur nec.</p>
  </section>

  <section class="pouch pouch--back">
    <svg class="back-art" width="462" height="684" viewBox="0 0 462 684">
      <path role="img" aria-label="Illustration of large tea leaves rising from the lower left"
            d="M0,500 C40,470 90,470 140,500 C170,520 185,560 175,600 C165,640 150,670 130,684 L0,684 Z"
            fill="var(--tea-teal)" opacity="0.85"/>
      <path role="img" aria-label="Illustration of large tea leaves rising from the lower right"
            d="M462,480 C420,490 380,520 350,560 C320,600 300,640 295,684 L462,684 Z"
            fill="var(--tea-teal)" opacity="0.85"/>
    </svg>
    <div class="tea-label">Lorem ipsum</div>
    <div class="zip-seal"></div>
    <div class="brand">
      <div class="brand__square"></div>
      <div class="brand__name">Vel Sarna</div>
    </div>
    <p class="back-copy">Lorem ipsum dolor sit amet,<br>an harum nominavi<br>vulputate duo, qui ne legere<br>tempor ocurreret, at rebum<br>feugait percipitur nec.</p>
    <div class="brew-steps">
      <div class="brew-step">
        <svg width="32" height="36" viewBox="0 0 32 36">
          <path d="M8,6 q3,-3 0,-6 M13,6 q3,-3 0,-6" stroke="var(--logo-ink)" stroke-width="1.5" fill="none"/>
          <rect x="6" y="12" width="16" height="14" rx="3" fill="var(--logo-ink)"/>
          <path d="M22,15 h4 v6 h-4" stroke="var(--logo-ink)" stroke-width="2" fill="none"/>
          <rect x="2" y="29" width="28" height="2" fill="var(--logo-ink)"/>
        </svg>
        <span class="brew-step__label">100°C</span>
      </div>
      <div class="brew-step">
        <svg width="32" height="36" viewBox="0 0 32 36">
          <path d="M18,0 l10,6 l-5,6 l-8,-4 z" fill="none" stroke="var(--logo-ink)" stroke-width="1.5"/>
          <rect x="6" y="14" width="16" height="12" rx="3" fill="var(--logo-ink)"/>
          <path d="M22,16 h4 v6 h-4" stroke="var(--logo-ink)" stroke-width="2" fill="none"/>
          <rect x="2" y="29" width="28" height="2" fill="var(--logo-ink)"/>
        </svg>
        <span class="brew-step__label">3g/250ml</span>
      </div>
      <div class="brew-step">
        <svg width="32" height="36" viewBox="0 0 32 36">
          <circle cx="16" cy="6" r="6" fill="none" stroke="var(--logo-ink)" stroke-width="1.5"/>
          <path d="M16,6 V0 A6,6 0 0 1 22,6 Z" fill="var(--logo-ink)"/>
          <rect x="6" y="14" width="16" height="12" rx="3" fill="var(--logo-ink)"/>
          <path d="M22,16 h4 v6 h-4" stroke="var(--logo-ink)" stroke-width="2" fill="none"/>
          <rect x="2" y="29" width="28" height="2" fill="var(--logo-ink)"/>
        </svg>
        <span class="brew-step__label">3 min</span>
      </div>
    </div>
    <div class="net-weight">150 gr</div>
    <div class="certs">
      <div class="cert-badge" role="img" aria-label="KWR certificate badge"></div>
      <div class="cert-badge" role="img" aria-label="HPM certificate badge"></div>
    </div>
  </section>

</body>
</html>
```